Penny auction website for high end market

need a penny auction web design , requirement as below :-

- classy and noble, as i am only selli high end products
- 25 products for the main page , 5 products per row ( please see sample picture )
- top 5 products can be highlighted as those are limited edition products
- main page , products page, members page , faq and about us page
- matching logo with the name lotvo
- clean
- responsive for desktoop
-mobile version
Updates

i missed the mobile version, i should get the mobile version aswell, for desktop it should be responsive Added Wednesday, August 16, 2017

designer may use gold or silver color too as i am selling only high end products exclusively for members only, the layout can be different than the sample, it just a guide line for the sample, other better layout would be great to see and to have.

some idea how highend feel to me https://img.kravenstock.example/scr/51200/shimmering-gem-layout-template_51277-original.jpg

guys, please use this design https://www.layoutquarry.example/site-templates/51277.html as the base , i want it high class and up market, thanks

Target Market(s)

highend products buyer

Number of Pages Required

5+ page

Font styles to use
Serif
Sans Serif
Script
Other font styles liked:
• designer match it

Colors

Designer to choose colors to be used in the design.

Requirements
Must have
• source code, logos ( use lotvo for now, will change later when confirm ) , PSD
Nice to have
• more different type of designs would be great, designers can present they ideas other than my requirement

```html
<!DOCTYPE html>
<html lang="en">
<head>
<meta charset="utf-8">
<title>lotvo — Penny Auctions</title>
<link href="https://fonts.googleapis.com/css2?family=Playfair+Display:wght@500;700&family=Roboto:wght@400;500;700&display=swap" rel="stylesheet">
<style>
:root{
  --black:#111214;
  --charcoal:#1c1d21;
  --graphite:#2a2b30;
  --gold:#c9a45a;
  --gold-light:#e8cf8f;
  --gold-deep:#9c7a36;
  --champagne:#f3e7c9;
  --silver:#c8cbd0;
  --silver-light:#eef0f2;
  --ink:#1e1e1e;
  --muted:#7a7a7a;
  --line:#e3e3e3;
  --white:#fff;
}
*{box-sizing:border-box;margin:0;padding:0}
html,body{width:1200px;height:2830px;overflow:hidden}
body{font-family:"Roboto",Arial,sans-serif;color:var(--ink);background:var(--white);position:relative}

/* top bar */
.topbar{position:absolute;left:0;top:0;width:1200px;height:42px;background:var(--black);color:var(--silver-light);font-size:13px;display:flex;align-items:center;justify-content:flex-end;padding-right:34px;gap:22px;border-bottom:1px solid var(--gold-deep)}
.accept{display:flex;align-items:center;gap:6px}
.card-chip{width:28px;height:17px;border-radius:2px;background:var(--silver)}
.card-chip.gold{background:var(--gold)}
.card-chip.pale{background:var(--silver-light)}
.cart{display:flex;align-items:center;gap:6px}
.menu-icon{width:18px;height:14px;display:flex;flex-direction:column;justify-content:space-between}
.menu-icon span{height:3px;background:var(--gold-light);border-radius:1px}

/* hero */
.hero{position:absolute;left:0;top:42px;width:1200px;height:445px;background:radial-gradient(circle at 70% 40%,#3a3325 0,var(--charcoal) 50%,var(--black) 100%);overflow:hidden}
.brand{position:absolute;left:108px;top:36px;width:94px;height:94px;border-radius:50%;background:var(--gold);display:flex;align-items:center;justify-content:center;color:var(--black);font-size:27px;font-weight:700}
.hero-title{position:absolute;left:100px;top:272px;color:var(--white);font-family:"Playfair Display",Georgia,serif;font-size:44px;font-weight:500;line-height:52px}
.hero-visual{position:absolute;left:368px;top:16px;width:727px;height:405px;border-radius:6px;background:linear-gradient(135deg,#6b6f76,#2b2d31 55%,#8a6d32)}

/* steps */
.steps{position:absolute;left:0;top:487px;width:1200px;height:47px;display:flex;gap:4px;background:var(--white)}
.step{flex:1;background:linear-gradient(#efe2c0,#dcc38a);display:flex;align-items:center;justify-content:center;font-size:16px;color:var(--ink)}
.step.start{background:var(--black);color:var(--gold-light);font-weight:500;text-transform:uppercase}

/* search */
.search{position:absolute;left:100px;top:600px;display:flex;height:45px}
.search-field{width:415px;border:1px solid var(--line);font-size:12px;color:#999;padding-left:18px;display:flex;align-items:center}
.search-btn{width:128px;background:var(--black);color:var(--white);font-size:13px;font-weight:700;letter-spacing:1px;display:flex;align-items:center;justify-content:center}
.category{position:absolute;left:796px;top:600px;width:304px;height:45px;background:linear-gradient(var(--gold-light),var(--gold));color:var(--black);font-size:13px;font-weight:700;letter-spacing:1px;display:flex;align-items:center;justify-content:space-between;padding:0 18px}

/* grid */
.products{position:absolute;left:100px;top:690px;width:1000px;display:grid;grid-template-columns:repeat(5,1fr);column-gap:13px;row-gap:12px}
.product{position:relative;height:323px;border:1px solid #e8e8e8;box-shadow:0 0 4px rgba(0,0,0,.08);display:flex;flex-direction:column;align-items:center;padding-top:20px;background:var(--white)}
.product.limited{border:2px solid var(--gold);background:linear-gradient(#fbf6ea,#fff 60%);box-shadow:0 2px 10px rgba(156,122,54,.25)}
.product.limited::before{content:"";position:absolute;top:-2px;right:14px;width:16px;height:24px;background:var(--gold);clip-path:polygon(0 0,100% 0,100% 100%,50% 72%,0 100%)}
.product-name{font-size:13px;font-weight:500;text-transform:uppercase;height:20px}
.product-photo{width:160px;height:86px;margin-top:12px;border:1px solid #ddd}
.stars{margin-top:18px;font-size:11px;color:var(--gold);letter-spacing:2px}
.timer{margin-top:12px;width:113px;height:23px;background:var(--silver-light);border-radius:2px;font-size:13px;color:var(--muted);letter-spacing:2px;display:flex;align-items:center;justify-content:center}
.value{margin-top:14px;font-size:17px;color:var(--gold-deep)}
.bid{margin-top:12px;width:113px;height:26px;background:var(--graphite);border-radius:2px;color:var(--white);font-size:11px;display:flex;align-items:center;justify-content:center}
.limited .bid{background:linear-gradient(var(--gold-light),var(--gold));color:var(--black)}

.tone-silver{background:linear-gradient(135deg,#eceef0,#8a8f96)}
.tone-red{background:linear-gradient(135deg,#f4f4f4,#b8262d)}
.tone-blue{background:linear-gradient(135deg,#d6e6f2,#2b5a8f)}
.tone-dark{background:linear-gradient(135deg,#e0e0e0,#1c1c1c)}
.tone-screen{background:linear-gradient(135deg,#2a4a9a,#e39a3a 60%,#111)}
.tone-warm{background:linear-gradient(135deg,#f3efe9,#8a6a3c)}
.tone-light{background:linear-gradient(135deg,#f7f7f7,#cfcfcf)}
.tone-pink{background:linear-gradient(135deg,#e2f0f4,#c77fae)}

/* newsletter */
.newsletter{position:absolute;left:0;top:2421px;width:1200px;height:72px;background:linear-gradient(90deg,var(--gold-deep),var(--gold) 50%,var(--gold-deep));display:flex;align-items:center}
.news-title{margin-left:115px;color:var(--black);font-size:19px;font-weight:500;text-transform:uppercase;width:264px}
.news-field{width:480px;height:38px;background:var(--white);font-size:12px;color:#999;padding-left:14px;display:flex;align-items:center}
.news-link{margin-left:32px;color:var(--black);font-size:19px;font-weight:500;text-decoration:underline}

/* footer */
.footer{position:absolute;left:0;top:2493px;width:1200px;height:268px;background:var(--charcoal);color:#d4d4d4;font-size:12px}
.foot-col{position:absolute;top:48px}
.foot-col h4{font-size:12px;font-weight:500;color:var(--gold-light);text-transform:uppercase;margin-bottom:22px}
.col-service{left:100px}
.col-about{left:319px;width:290px}
.col-contact{left:687px;width:250px}
.col-follow{left:979px}
.links li{list-style:none;margin-bottom:14px;display:flex;align-items:center;gap:16px}
.links span{color:var(--gold)}
.about{line-height:24px}
.contact-row{display:flex;gap:18px;margin-bottom:22px;line-height:22px}
.contact-row svg{flex:none;margin-top:4px}
.socials{display:flex;gap:10px}
.socials span{width:34px;height:34px;border-radius:50%;background:var(--silver)}
.bottom{position:absolute;left:0;top:2761px;width:1200px;height:69px;background:var(--black);color:#bbb;font-size:12px;display:flex;align-items:center;justify-content:center}
</style>
</head>
<body>

<header class="topbar">
  <div class="accept">We Accept : <span class="card-chip"></span><span class="card-chip gold"></span><span class="card-chip pale"></span></div>
  <div class="cart">Shopping cart :
    <svg width="18" height="16" viewBox="0 0 18 16"><path d="M1 2h3l2 8h9l2-6H5" fill="none" stroke="#e8cf8f" stroke-width="1.6"/><circle cx="7" cy="13.5" r="1.5" fill="#e8cf8f"/><circle cx="14" cy="13.5" r="1.5" fill="#e8cf8f"/></svg>0</div>
  <div class="menu-icon"><span></span><span></span><span></span></div>
</header>

<section class="hero">
  <div class="brand">lotvo</div>
  <div class="hero-visual" role="img" aria-label="Collage of premium products on sale: curved TV, tablet and phone, laptop, camera and fragrance with sale tags"></div>
  <h1 class="hero-title">We sell high<br>end products</h1>
</section>

<nav class="steps">
  <div class="step">1.Create an Account</div>
  <div class="step">2.Choose your products</div>
  <div class="step">3.Bid and Win</div>
  <div class="step start">Start now</div>
</nav>

<div class="search">
  <div class="search-field">Search Products..</div>
  <div class="search-btn">SEARCH</div>
</div>
<div class="category">ALL CATEGORIES
  <svg width="10" height="6" viewBox="0 0 10 6"><path d="M0 0h10L5 6z" fill="#111214"/></svg>
</div>

<main class="products">
  <article class="product limited"><h3 class="product-name">Sed perspiciatis</h3><div class="product-photo tone-silver" role="img" aria-label="Smartphone"></div><div class="stars">★★★★</div><div class="timer">00:00:98</div><div class="value">Value $53.78</div><div class="bid">Bid Now | X3</div></article>
  <article class="product limited"><h3 class="product-name">Edut perspicias</h3><div class="product-photo tone-red" role="img" aria-label="Red compact camera"></div><div class="stars">★★★★</div><div class="timer">00:00:98</div><div class="value">Value $53.78</div><div class="bid">Bid Now | X3</div></article>
  <article class="product limited"><h3 class="product-name">Minim veniam</h3><div class="product-photo tone-blue" role="img" aria-label="Professional video camera"></div><div class="stars">★★★★</div><div class="timer">00:00:98</div><div class="value">Value $53.78</div><div class="bid">Bid Now | X3</div></article>
  <article class="product limited"><h3 class="product-name">Unde omnis iste</h3><div class="product-photo tone-dark" role="img" aria-label="Pair of speakers"></div><div class="stars">★★★★</div><div class="timer">00:00:98</div><div class="value">Value $53.78</div><div class="bid">Bid Now | X3</div></article>
  <article class="product limited"><h3 class="product-name">Magni dolores eos</h3><div class="product-photo tone-screen" role="img" aria-label="Video wall of screens"></div><div class="stars">★★★★</div><div class="timer">00:00:98</div><div class="value">Value $53.78</div><div class="bid">Bid Now | X3</div></article>

  <article class="product"><h3 class="product-name">Sed perspiciatis</h3><div class="product-photo tone-light" role="img" aria-label="Camera on tripod"></div><div class="stars">★★★★</div><div class="timer">00:00:98</div><div class="value">Value $53.78</div><div class="bid">Bid Now | X3</div></article>
  <article class="product"><h3 class="product-name">Magni dolores eos</h3><div class="product-photo tone-warm" role="img" aria-label="Projector"></div><div class="stars">★★★★</div><div class="timer">00:00:98</div><div class="value">Value $53.78</div><div class="bid">Bid Now | X3</div></article>
  <article class="product"><h3 class="product-name">Sed perspiciatis</h3><div class="product-photo tone-blue" role="img" aria-label="Flat screen television"></div><div class="stars">★★★★</div><div class="timer">00:00:98</div><div class="value">Value $53.78</div><div class="bid">Bid Now | X3</div></article>
  <article class="product"><h3 class="product-name">Magni dolores eos</h3><div class="product-photo tone-warm" role="img" aria-label="Light bulb"></div><div class="stars">★★★★</div><div class="timer">00:00:98</div><div class="value">Value $53.78</div><div class="bid">Bid Now | X3</div></article>
  <article class="product"><h3 class="product-name">Sed perspiciatis</h3><div class="product-photo tone-dark" role="img" aria-label="Smartphone"></div><div class="stars">★★★★</div><div class="timer">00:00:98</div><div class="value">Value $53.78</div><div class="bid">Bid Now | X3</div></article>

  <article class="product"><h3 class="product-name">Exerction ullamco</h3><div class="product-photo tone-warm" role="img" aria-label="Fragrance bottles"></div><div class="stars">★★★★</div><div class="timer">00:00:98</div><div class="value">Value $53.78</div><div class="bid">Bid Now | X3</div></article>
  <article class="product"><h3 class="product-name">Sed perspiciatis</h3><div class="product-photo tone-blue" role="img" aria-label="Group of smartphones"></div><div class="stars">★★★★</div><div class="timer">00:00:98</div><div class="value">Value $53.78</div><div class="bid">Bid Now | X3</div></article>
  <article class="product"><h3 class="product-name">Magni dolores eos</h3><div class="product-photo tone-light" role="img" aria-label="Cosmetic bottles"></div><div class="stars">★★★★</div><div class="timer">00:00:98</div><div class="value">Value $53.78</div><div class="bid">Bid Now | X3</div></article>
  <article class="product"><h3 class="product-name">Sed perspiciatis</h3><div class="product-photo tone-screen" role="img" aria-label="Row of monitors"></div><div class="stars">★★★★</div><div class="timer">00:00:98</div><div class="value">Value $53.78</div><div class="bid">Bid Now | X3</div></article>
  <article class="product"><h3 class="product-name">Ercitation ullamco</h3><div class="product-photo tone-dark" role="img" aria-label="Classic camera"></div><div class="stars">★★★★</div><div class="timer">00:00:98</div><div class="value">Value $53.78</div><div class="bid">Bid Now | X3</div></article>

  <article class="product"><h3 class="product-name">Magni dolores eos</h3><div class="product-photo tone-screen" role="img" aria-label="Wall of televisions"></div><div class="stars">★★★★</div><div class="timer">00:00:98</div><div class="value">Value $53.78</div><div class="bid">Bid Now | X3</div></article>
  <article class="product"><h3 class="product-name">Sed perspiciatis</h3><div class="product-photo tone-red" role="img" aria-label="Television showing flowers"></div><div class="stars">★★★★</div><div class="timer">00:00:98</div><div class="value">Value $53.78</div><div class="bid">Bid Now | X3</div></article>
  <article class="product"><h3 class="product-name">Sed perspiciatis</h3><div class="product-photo tone-light" role="img" aria-label="Makeup set"></div><div class="stars">★★★★</div><div class="timer">00:00:98</div><div class="value">Value $53.78</div><div class="bid">Bid Now | X3</div></article>
  <article class="product"><h3 class="product-name">Magni dolores eos</h3><div class="product-photo tone-blue" role="img" aria-label="Set of devices"></div><div class="stars">★★★★</div><div class="timer">00:00:98</div><div class="value">Value $53.78</div><div class="bid">Bid Now | X3</div></article>
  <article class="product"><h3 class="product-name">Sed perspiciatis</h3><div class="product-photo tone-dark" role="img" aria-label="Camera lens"></div><div class="stars">★★★★</div><div class="timer">00:00:98</div><div class="value">Value $53.78</div><div class="bid">Bid Now | X3</div></article>

  <article class="product"><h3 class="product-name">Sed perspiciatis</h3><div class="product-photo tone-pink" role="img" aria-label="Perfume bottle"></div><div class="stars">★★★★</div><div class="timer">00:00:98</div><div class="value">Value $53.78</div><div class="bid">Bid Now | X3</div></article>
  <article class="product"><h3 class="product-name">Magni dolores eos</h3><div class="product-photo tone-warm" role="img" aria-label="Film projector"></div><div class="stars">★★★★</div><div class="timer">00:00:98</div><div class="value">Value $53.78</div><div class="bid">Bid Now | X3</div></article>
  <article class="product"><h3 class="product-name">Exercitation lamco</h3><div class="product-photo tone-dark" role="img" aria-label="Hi-fi sound system"></div><div class="stars">★★★★</div><div class="timer">00:00:98</div><div class="value">Value $53.78</div><div class="bid">Bid Now | X3</div></article>
  <article class="product"><h3 class="product-name">Sed perspiciatis</h3><div class="product-photo tone-blue" role="img" aria-label="Laptop"></div><div class="stars">★★★★</div><div class="timer">00:00:98</div><div class="value">Value $53.78</div><div class="bid">Bid Now | X3</div></article>
  <article class="product"><h3 class="product-name">Magni dolores eos</h3><div class="product-photo tone-warm" role="img" aria-label="Vintage radio"></div><div class="stars">★★★★</div><div class="timer">00:00:98</div><div class="value">Value $53.78</div><div class="bid">Bid Now | X3</div></article>
</main>

<section class="newsletter">
  <h2 class="news-title">Join our news letter</h2>
  <div class="news-field">Email</div>
  <a class="news-link">Get Instant Access</a>
</section>

<footer class="footer">
  <div class="foot-col col-service">
    <h4>Customer Service</h4>
    <ul class="links">
      <li><span>»</span>contact us</li>
      <li><span>»</span>Delivery &amp; returns</li>
      <li><span>»</span>Warranties &amp;repairs</li>
      <li><span>»</span>Price match promise</li>
      <li><span>»</span>New visitor guide</li>
    </ul>
  </div>
  <div class="foot-col col-about">
    <h4>About Us</h4>
    <p class="about">Lorem ipsum dolor sit amet, consectetur adipiscing elit, quis nostrud exercitation ullamco laboris nisi ut aliquip ex ed tempor iquis nostrud exercitation ullamco laboris nisi ut aliquip ex encididunt ut labore et dolore magquis nostrud exercitation ullam-co aliquimd mm veniam.</p>
  </div>
  <div class="foot-col col-contact">
    <h4>Contact Us</h4>
    <div class="contact-row"><svg width="14" height="12" viewBox="0 0 14 12"><path d="M7 0l7 6h-2v6H9V8H5v4H2V6H0z" fill="#c9a45a"/></svg><span>2280 Orchard Vale Rd, Suite 40<br>Fernhill 50718</span></div>
    <div class="contact-row"><svg width="9" height="14" viewBox="0 0 9 14"><rect x="0.8" y="0.8" width="7.4" height="12.4" rx="1.2" fill="none" stroke="#c9a45a" stroke-width="1.4"/><circle cx="4.5" cy="11" r=".9" fill="#c9a45a"/></svg><span>Phone : (555) - 014 - 2270</span></div>
    <div class="contact-row"><svg width="14" height="10" viewBox="0 0 14 10"><rect x=".7" y=".7" width="12.6" height="8.6" fill="none" stroke="#c9a45a" stroke-width="1.4"/><path d="M1 1l6 5 6-5" fill="none" stroke="#c9a45a" stroke-width="1.4"/></svg><span>hello@lotvo.example</span></div>
  </div>
  <div class="foot-col col-follow">
    <h4>Follow Us</h4>
    <div class="socials"><span></span><span></span><span></span></div>
  </div>
</footer>
<div class="bottom">© copyright 2017 lotvo . All rights reserved &nbsp;|&nbsp; Privacy policy</div>

</body>
</html>
```